Graphic Design Assets for Brash Ward – Wellness with a Rock 'n' Roll Edge

Forget clinical blue, pastel gradients, and soft corporate stock photos. Brash Ward is a movement shattering the traditional, sterile look of mental health and wellness. We need a designer with a youthful, high-signal, rock 'n' roll design sensibility; someone who understands grit, physical presence, and bold editorial design. If your aesthetic is closer to a classic vinyl gatefold or a gritty street brand than a pharmacy brochure, we want you.

Project Overview
We have a finalized brand book and a clear creative direction. What we need now is a killer suite of graphic design assets to break up text-heavy layouts and bring our brand to life across three core touchpoints: a new website, a pitch/presentation deck, and a downloadable lead-gen asset (White Paper).

We are looking for the design assets first. If you have UI/UX or layout skills, you can handle the full implementation of the deck and document. If you are strictly a visual asset designer, you can deliver the components for our web developer to build with.

Scope of Work & Deliverables
We need a cohesive set of visual assets, including:

Web & UI Assets: Custom iconography, striking section dividers, bold typographic styling elements, and graphic textures to turn a text-heavy website into an immersive user experience.

Presentation Elements: Master slide backgrounds, data visualization graphics, and framing assets to transform a standard 10-page presentation deck.

Editorial Layout Assets: Headers, callout box designs, and spot graphics to make a downloadable White Paper look like a premium, tactical, independent magazine.

Design Sensibility & Brand Vibe
The Aesthetic: Utilitarian, gritty, tactile, and high-signal. Think bold typography, stark contrast, and raw authenticity. Think punk rock or liberation propaganda.

What to Avoid: Standard corporate tech design, clinical/medical visuals, soft "self-help" tropes, and generic minimalist vectors.

Target Audience: Young men, mentors, and partners who value real-world agency, movement, and zero fluff.

```html
<!DOCTYPE html>
<html lang="en">
<head>
<meta charset="utf-8">
<title>Brash Ward — Visual Identity Board</title>
<link href="https://fonts.googleapis.com/css2?family=Anton&family=Oswald:wght@500;700&family=Space+Mono:wght@400;700&family=Archivo+Narrow:wght@500;700&family=Caveat:wght@600&family=Special+Elite&display=swap" rel="stylesheet">
<style>
:root{
  --off-black:#0D0D0D;
  --panel:#0a0a0a;
  --line:#2e2e2e;
  --bone:#F2F0E8;
  --paper:#e4dfd2;
  --concrete:#8E8E8E;
  --orange:#FF5A1F;
  --acid:#E6FF00;
  --red:#D90404;
  --green:#2E7D32;
  --ink:#111;
}
*{margin:0;padding:0;box-sizing:border-box}
html,body{width:1200px;height:800px;overflow:hidden;background:#050505}
.board{position:absolute;left:0;top:0;width:1536px;height:1024px;transform:scale(.78125);transform-origin:0 0;background:#050505;color:var(--bone);font-family:"Space Mono",monospace}
.a{position:absolute}
.panel{position:absolute;background:var(--panel);border:1px solid var(--line);overflow:hidden}
.p-title{position:absolute;left:10px;top:6px;font:700 15px/1.2 "Oswald",sans-serif;letter-spacing:.3px;text-transform:uppercase;color:var(--bone)}
.p-sub{position:absolute;left:10px;top:25px;font:400 9px/1.35 "Space Mono",monospace;letter-spacing:.4px;text-transform:uppercase;color:#cfcbc0}
.mono{font-family:"Space Mono",monospace;text-transform:uppercase;letter-spacing:.4px}
.tiny{font-size:7.5px;line-height:1.3}
.small{font-size:9px;line-height:1.3}
.display{font-family:"Anton",sans-serif;text-transform:uppercase;line-height:.88;letter-spacing:-.5px;white-space:nowrap}
.cond{font-family:"Oswald",sans-serif;text-transform:uppercase}
.brandname{font:700 9px/1 "Space Mono",monospace;text-transform:uppercase;letter-spacing:.5px;display:flex;align-items:center;gap:5px}
.brandname i{display:inline-block;width:7px;height:7px;background:currentColor}
.box{position:absolute;border:1px solid #3a3a3a;background:#101010;overflow:hidden}
.box-label{position:absolute;left:10px;top:5px;font:400 8px/1 "Space Mono",monospace;text-transform:uppercase;letter-spacing:.5px;color:#ddd}
.tile-label{position:absolute;font:400 7.5px/1 "Space Mono",monospace;text-transform:uppercase;color:#ddd}
.tex{position:absolute;border:1px solid #222}
.photo{position:absolute}
.card{position:absolute;overflow:hidden}
.swatch{position:absolute;padding:8px;display:flex;flex-direction:column;justify-content:flex-end;font:400 8px/1.35 "Space Mono",monospace;text-transform:uppercase}
.footer{position:absolute;left:0;top:992px;width:1536px;height:32px;border-top:1px solid #222;background:#050505}
</style>
</head>
<body>
<div class="board">

<!-- 01 TYPOGRAPHY -->
<section class="panel" style="left:10px;top:10px;width:505px;height:418px">
  <h2 class="p-title">01. Typography Direction</h2>
  <p class="p-sub">Bold. Condensed. Impactful.<br>Type that commands attention.</p>
  <div class="a display" style="left:10px;top:60px;font-size:76px;line-height:.9;letter-spacing:-1.5px;color:var(--bone)">Real<br>World<br>Recovery.</div>
  <div class="a brandname" style="left:14px;top:285px;color:#ddd"><i></i>Brash Ward</div>
  <div class="a" style="left:296px;top:26px;width:1px;height:275px;background:#333"></div>
  <div class="a mono tiny" style="left:308px;top:24px;color:#ccc">Primary display</div>
  <div class="a cond" style="left:308px;top:34px;font-size:19px;font-weight:500">Breaker Condensed</div>
  <div class="a mono" style="left:308px;top:60px;font-size:9px;font-weight:700;letter-spacing:1.6px">ABCDEFGHIJKLMNOPQRSTUWXYZ<br>0123456789</div>
  <div class="a mono tiny" style="left:308px;top:104px;color:#ccc">Secondary</div>
  <div class="a" style="left:308px;top:116px;font:500 13px/1 'Archivo Narrow',sans-serif;text-transform:uppercase;letter-spacing:.4px">Yardline Gothic Condensed</div>
  <div class="a mono tiny" style="left:308px;top:136px;letter-spacing:.5px">ABCDEFGHIJKLMNOPQRSTUVWXYZ<br>0123456789</div>
  <div class="a mono tiny" style="left:308px;top:178px;color:#ccc">Accent / details</div>
  <div class="a" style="left:308px;top:191px;font:500 12px/1 'Archivo Narrow',sans-serif;text-transform:uppercase;letter-spacing:.5px">Plantwork Grotesk</div>
  <div class="a mono" style="left:308px;top:210px;font-size:7px;line-height:1.4">ABCDEFGHIJKLMNOPQRSTUVWXYZ<br>0123456789</div>

  <div class="card" style="left:13px;top:305px;width:117px;height:105px;background:var(--orange);color:var(--ink)">
    <div class="a display" style="left:6px;top:6px;font-size:38px">Move<br>First.</div>
    <div class="a mono" style="left:6px;bottom:5px;font-size:6.5px;font-weight:700">Brash Ward</div>
  </div>
  <div class="card" style="left:137px;top:305px;width:115px;height:105px;background:#0d0d0d;border:1px solid #333">
    <div class="a display" style="left:5px;top:6px;font-size:28px;letter-spacing:-.8px">No<br>Numbing.</div>
    <div class="a mono" style="left:5px;bottom:5px;font-size:6.5px;color:#ccc">Brash Ward</div>
  </div>
  <div class="card" style="left:261px;top:305px;width:109px;height:105px;background:var(--acid);color:var(--ink)">
    <div class="a display" style="left:6px;top:5px;font-size:31px;line-height:.86">Built<br>Not<br>Fixed.</div>
  </div>
  <div class="card" style="left:379px;top:305px;width:114px;height:105px;background:#0d0d0d;border:1px solid #333">
    <div class="a display" style="left:6px;top:6px;font-size:31px;letter-spacing:-.8px">This is<br>on you.</div>
    <div class="a mono" style="left:6px;bottom:5px;font-size:6.5px;color:#ccc">Brash Ward</div>
  </div>
</section>

<!-- 02 TEXTURES -->
<section class="panel" style="left:524px;top:10px;width:476px;height:418px">
  <h2 class="p-title">02. Texture &amp; Graphic Treatments</h2>
  <p class="p-sub">Grit. Tactility. Imperfection.<br>Makes it real.</p>
  <div class="tex" role="img" aria-label="Xerox grain texture" style="left:12px;top:60px;width:108px;height:85px;background:radial-gradient(circle,#2a2a2a,#0b0b0b)"></div>
  <div class="tile-label" style="left:12px;top:150px">Xerox grain</div>
  <div class="tex" role="img" aria-label="Halftone dot texture" style="left:128px;top:60px;width:107px;height:85px;background:linear-gradient(135deg,#ddd,#555)"></div>
  <div class="tile-label" style="left:128px;top:150px">Halftone</div>
  <div class="tex" role="img" aria-label="Ink distress texture" style="left:243px;top:60px;width:107px;height:85px;background:radial-gradient(circle at 45% 45%,#111 35%,#d8d5cc 75%)"></div>
  <div class="tile-label" style="left:243px;top:150px">Ink distress</div>
  <div class="tex" role="img" aria-label="Torn paper edge texture" style="left:359px;top:60px;width:105px;height:85px;background:linear-gradient(180deg,#cfc6b3 55%,#3a362f 56%,#1a1a1a)"></div>
  <div class="tile-label" style="left:359px;top:150px">Paper edge</div>

  <div class="tex" role="img" aria-label="Tape marks texture" style="left:12px;top:165px;width:108px;height:78px;background:linear-gradient(160deg,#d6d3ca,#8f8c85)"></div>
  <div class="tile-label" style="left:12px;top:248px">Tape marks</div>
  <div class="tex" style="left:128px;top:165px;width:107px;height:78px;background:#dcd9d0">
    <div class="a" style="left:24px;top:9px;width:60px;height:60px;border:2px solid #222;border-radius:50%"></div>
    <div class="a mono" style="left:24px;top:30px;width:60px;text-align:center;font-size:7px;font-weight:700;color:#222;line-height:1.3">Brash Ward<br>Est. 2024</div>
  </div>
  <div class="tile-label" style="left:128px;top:248px">Stamp texture</div>
  <div class="tex" role="img" aria-label="Spray paint texture" style="left:243px;top:165px;width:107px;height:78px;background:radial-gradient(circle,#333 10%,#cfccc3 60%)"></div>
  <div class="tile-label" style="left:243px;top:248px">Spray paint</div>
  <div class="tex" role="img" aria-label="Newsprint texture" style="left:359px;top:165px;width:105px;height:78px;background:linear-gradient(180deg,#bdb9ae,#8d8a82)"></div>
  <div class="tile-label" style="left:359px;top:248px">Newsprint</div>

  <div class="tex" role="img" aria-label="Stencil lettering texture" style="left:12px;top:262px;width:108px;height:92px;background:linear-gradient(160deg,#cfccc3,#8a877f)"></div>
  <div class="tile-label" style="left:12px;top:360px">Stencil</div>
  <div class="tex" role="img" aria-label="Scratch and scuff texture" style="left:128px;top:262px;width:107px;height:92px;background:radial-gradient(circle,#333,#0d0d0d)"></div>
  <div class="tile-label" style="left:128px;top:360px">Scratch / scuff</div>
  <div class="tex" style="left:243px;top:262px;width:107px;height:92px;background:#e6e3da">
    <div class="a" style="left:10px;top:12px;width:86px;height:8px;background:#111"></div>
    <div class="a" style="left:10px;top:27px;width:60px;height:8px;background:#111"></div>
    <div class="a" style="left:10px;top:42px;width:80px;height:8px;background:#111"></div>
    <div class="a" style="left:10px;top:57px;width:70px;height:8px;background:#111"></div>
    <div class="a" style="left:10px;top:72px;width:50px;height:8px;background:#111"></div>
  </div>
  <div class="tile-label" style="left:243px;top:360px">Redaction</div>
  <div class="tex" role="img" aria-label="Folded paper texture" style="left:359px;top:262px;width:105px;height:92px;background:linear-gradient(135deg,#c9c6bf,#9a978f 50%,#c4c1ba)"></div>
  <div class="tile-label" style="left:359px;top:360px">Folded paper</div>
</section>

<!-- 03 COLOR -->
<section class="panel" style="left:1008px;top:10px;width:518px;height:418px">
  <h2 class="p-title">03. Color System</h2>
  <p class="p-sub">Limited. High contrast.<br>Used with intent.</p>
  <div class="a mono tiny" style="left:10px;top:56px">Base</div>
  <div class="swatch" style="left:10px;top:68px;width:122px;height:80px;background:var(--off-black);border:1px solid #444;color:#ddd">Off-black<br>#0D0D0D</div>
  <div class="swatch" style="left:140px;top:68px;width:124px;height:80px;background:var(--bone);color:#222">Bone white<br>#F2F0E8</div>
  <div class="swatch" style="left:272px;top:68px;width:125px;height:80px;background:var(--concrete);color:#222">Concrete gray<br>#8E8E8E</div>
  <div class="a mono tiny" style="left:10px;top:158px">Signal colors (use sparingly)</div>
  <div class="swatch" style="left:10px;top:172px;width:119px;height:76px;background:var(--orange);color:#222">Safety orange<br>#FF5A1F</div>
  <div class="swatch" style="left:135px;top:172px;width:119px;height:76px;background:var(--acid);color:#222">Acid yellow<br>#E6FF00</div>
  <div class="swatch" style="left:260px;top:172px;width:119px;height:76px;background:var(--red);color:#eee">Blood red<br>#D90404</div>
  <div class="swatch" style="left:384px;top:172px;width:120px;height:76px;background:var(--green);color:#eee">Industrial green<br>#2E7D32</div>
  <div class="a mono tiny" style="left:10px;top:258px">Example usage</div>
  <div class="a" style="left:68px;top:262px;width:436px;height:1px;background:#333"></div>
  <div class="a" style="left:10px;top:272px;width:494px;height:138px;background:#141414;overflow:hidden">
    <div class="photo" role="img" aria-label="Athlete crouched low in training, orange-toned" style="left:200px;top:0;width:294px;height:138px;background:linear-gradient(90deg,#141414,#c2431a 30%,#8a2c10 70%,#2a0f06)"></div>
    <div class="a display" style="left:12px;top:24px;font-size:46px;letter-spacing:-1px;color:var(--bone)">Discipline<br>builds freedom.</div>
    <div class="a mono" style="right:10px;top:10px;font-size:11px;text-align:right;color:#eee">40.7128° N<br>74.0060° W</div>
    <div class="a" style="right:12px;bottom:12px;width:9px;height:9px;background:var(--orange)"></div>
  </div>
</section>

<!-- 04 PHOTOGRAPHY -->
<section class="panel" style="left:10px;top:436px;width:505px;height:332px">
  <h2 class="p-title">04. Photography Direction</h2>
  <p class="p-sub">Documentary. Raw. Human.<br>Real moments. Real environments.</p>
  <div class="photo" role="img" aria-label="Man running through a city street at dusk" style="left:6px;top:50px;width:110px;height:126px;background:linear-gradient(180deg,#3b4654,#1a1f26)"></div>
  <div class="photo" role="img" aria-label="Close portrait of a determined man, no smile" style="left:123px;top:50px;width:104px;height:126px;background:linear-gradient(180deg,#4a4038,#1b1714)"></div>
  <div class="photo" role="img" aria-label="Man training on a heavy bag in a dark gym" style="left:233px;top:50px;width:154px;height:126px;background:linear-gradient(135deg,#3a3733,#121110)"></div>
  <div class="photo" role="img" aria-label="Climber standing on rocks against grey sky" style="left:393px;top:50px;width:101px;height:126px;background:linear-gradient(180deg,#8a8a8a,#2b2b2b)"></div>
  <div class="photo" role="img" aria-label="Man carrying a log through a winter forest" style="left:6px;top:182px;width:125px;height:110px;background:linear-gradient(180deg,#9a9a98,#3a3833)"></div>
  <div class="photo" role="img" aria-label="Figure walking alone through a tunnel" style="left:138px;top:182px;width:114px;height:110px;background:radial-gradient(circle at 50% 40%,#777,#151515)"></div>
  <div class="photo" role="img" aria-label="Two hands clasping, chalked" style="left:258px;top:182px;width:118px;height:110px;background:linear-gradient(135deg,#6e6c68,#1e1d1b)"></div>
  <div class="photo" role="img" aria-label="Man in beanie outdoors, looking away" style="left:382px;top:182px;width:113px;height:110px;background:linear-gradient(135deg,#8f9294,#2d2b29)"></div>
  <div class="a mono small" style="left:10px;top:308px;font-size:9px"><span style="color:var(--orange)">Avoid:</span> staged, soft light, smiling stock photos, overly perfect images.</div>
</section>

<!-- 05 WEB ASSETS -->
<section class="panel" style="left:524px;top:436px;width:476px;height:332px">
  <h2 class="p-title">05. Web Asset Concepts</h2>
  <p class="p-sub">Visuals that create immersion and momentum.</p>
  <div class="box" style="left:9px;top:44px;width:277px;height:135px">
    <div class="box-label">Section dividers</div>
    <div class="a cond" style="left:0;top:14px;width:275px;height:34px;background:#d6d2c7;color:#111;font-size:13px;font-weight:700;padding:9px 0 0 24px">Move through discomfort</div>
    <div class="a" style="left:0;top:58px;width:275px;height:28px;background:repeating-linear-gradient(135deg,var(--orange) 0 16px,#111 16px 30px)"></div>
    <div class="a display" style="left:12px;top:92px;font-size:36px;color:#777;letter-spacing:1px">No excuses</div>
    <div class="a" style="left:10px;top:113px;width:232px;height:7px;background:var(--acid);opacity:.9"></div>
  </div>
  <div class="box" style="left:296px;top:44px;width:170px;height:135px">
    <div class="box-label" style="left:24px">Iconography</div>
    <svg class="a" style="left:8px;top:18px" width="155" height="100" viewBox="0 0 155 100" fill="none" stroke="#eee" stroke-width="2.4">
      <path d="M4 22 L14 6 L20 15 L24 9 L32 22 Z" fill="#eee"/>
      <path d="M50 6 L43 14 L50 22 M57 6 L50 14 L57 22"/>
      <path d="M65 6 L72 14 L65 22 M72 6 L79 14 L72 22"/>
      <circle cx="102" cy="14" r="8"/><path d="M102 2 v24 M90 14 h24"/>
      <path d="M136 4 l9 3 v7 c0 6 -4 9 -9 11 c-5 -2 -9 -5 -9 -11 v-7 z" fill="#eee"/>
      <rect x="8" y="42" width="14" height="14" rx="3" fill="#eee"/>
      <path d="M48 58 v-5 M54 58 v-9 M60 58 v-13 M44 58 h20"/>
      <path d="M90 50 q12 -10 24 0 q-12 10 -24 0 z"/><circle cx="102" cy="50" r="3" fill="#eee"/>
      <circle cx="136" cy="50" r="9"/><path d="M132 55 l6 -10 l-2 5z" fill="#eee"/>
      <path d="M8 76 l14 14 M22 76 l-14 14"/>
      <path d="M46 92 v-18 h14 l-3 4 l3 4 h-14"/>
    </svg>
    <div class="a mono" style="left:8px;bottom:4px;font-size:7px;color:#ccc">Industrial. Tactical. Functional.</div>
  </div>

  <div class="box" style="left:9px;top:186px;width:277px;height:140px">
    <div class="box-label">UI elements</div>
    <div class="a" style="left:8px;top:18px;width:80px;height:70px;background:#d9d5ca;color:#111;padding:6px 8px;font:500 13px/1.25 'Oswald',sans-serif;text-transform:uppercase">Focus<br><span style="color:var(--orange)">Execute</span><br>Repeat</div>
    <div class="a mono" style="left:94px;top:18px;width:80px;height:70px;background:#d9d5ca;color:#555;font-size:6.5px;padding:8px">40.7128° N<br>74.0060° W<br>Harbor City</div>
    <div class="a" style="left:178px;top:18px;width:96px;height:70px;background:#d9d5ca;color:#111">
      <div class="a display" style="left:6px;top:6px;font-size:30px">01</div>
      <div class="a mono" style="left:38px;top:24px;font-size:7px">/04</div>
      <svg class="a" style="left:10px;top:36px" width="80" height="32"><ellipse cx="40" cy="16" rx="36" ry="13" fill="none" stroke="var(--red)" stroke-width="2.5"/></svg>
    </div>
    <div class="a" style="left:0;top:94px;width:184px;height:44px;background:#0d0d0d"></div>
    <div class="a mono" style="left:10px;top:100px;font-size:9px;line-height:1.25">This is not<br>about feelings.<br>It's about <span style="background:var(--acid);color:#111;padding:0 2px">action.</span></div>
    <div class="a" style="left:184px;top:94px;width:92px;height:44px;background:#d9d5ca;color:#111;font:700 14px/44px sans-serif;text-align:center;letter-spacing:10px">→→→</div>
  </div>
  <div class="box" style="left:296px;top:186px;width:170px;height:140px">
    <div class="box-label" style="left:14px">Annotations / overlays</div>
    <div class="a" style="left:14px;top:18px;width:142px;height:84px;background:#d8d2c2;transform:rotate(-1.5deg)"></div>
    <div class="a" style="left:18px;top:16px;width:26px;height:10px;background:#1a1a1a;transform:rotate(-25deg)"></div>
    <div class="a" style="left:122px;top:94px;width:26px;height:10px;background:#1a1a1a;transform:rotate(-25deg)"></div>
    <div class="a" style="left:30px;top:34px;font:400 9px/1.3 'Special Elite',monospace;color:#111;text-transform:uppercase">Remember:<br>Nobody is<br>coming to<br>save you.</div>
    <div class="a" style="left:30px;top:114px;width:110px;height:12px;background:#111"></div>
  </div>
</section>

<!-- 06 DECK -->
<section class="panel" style="left:1008px;top:436px;width:518px;height:332px">
  <h2 class="p-title">06. Presentation Deck Style</h2>
  <p class="p-sub">A manifesto, not a corporate deck.</p>
  <div class="card" style="left:10px;top:44px;width:180px;height:170px;background:#0f0f0f;border:1px solid #333">
    <div class="a display" style="left:10px;top:18px;font-size:29px;line-height:.95;letter-spacing:-.8px">The system<br>wasn't built<br>for us.</div>
    <div class="a mono" style="left:10px;top:128px;font-size:9px;line-height:1.3">So we built<br>something better.</div>
    <div class="a" style="right:10px;bottom:10px;width:8px;height:8px;background:var(--orange)"></div>
  </div>
  <div class="card" style="left:197px;top:44px;width:173px;height:170px;background:var(--orange)">
    <div class="photo" role="img" aria-label="Lone man standing, seen from behind" style="left:90px;top:40px;width:83px;height:130px;background:linear-gradient(180deg,#c4431a,#5c1e0a)"></div>
    <div class="a display" style="left:10px;top:20px;font-size:32px;color:var(--bone)">Our<br>solution</div>
    <div class="a mono" style="left:10px;top:104px;font-size:7px;line-height:1.35;color:#fff">A movement.<br>A community.<br>A new standard<br>for men's<br>mental health.</div>
  </div>
  <div class="card" style="left:377px;top:44px;width:127px;height:170px;background:var(--bone);color:#111">
    <div class="a display" style="left:8px;top:8px;font-size:17px;line-height:.95">Real impact.<br>Real numbers.</div>
    <div class="a mono" style="left:8px;top:52px;font-size:6px;line-height:1.25"><b style="font-size:8px">78%</b><br>more active</div>
    <div class="a" style="left:46px;top:56px;width:62px;height:6px;background:#111"></div>
    <div class="a mono" style="left:8px;top:80px;font-size:6px;line-height:1.25"><b style="font-size:8px">64%</b><br>more resilient</div>
    <div class="a" style="left:46px;top:84px;width:50px;height:6px;background:var(--orange)"></div>
    <div class="a mono" style="left:8px;top:108px;font-size:6px;line-height:1.25"><b style="font-size:8px">53%</b><br>better bonds</div>
    <div class="a" style="left:46px;top:112px;width:40px;height:6px;background:var(--acid)"></div>
    <div class="a mono" style="left:8px;top:136px;font-size:6px;line-height:1.25"><b style="font-size:8px">91%</b><br>would refer</div>
    <div class="a" style="left:46px;top:140px;width:70px;height:6px;background:var(--green)"></div>
  </div>
  <div class="card" style="left:10px;top:222px;width:234px;height:106px;background:var(--bone);color:#111">
    <div class="a display" style="left:10px;top:8px;font-size:19px">Traction.</div>
    <div class="a mono" style="left:10px;top:34px;font-size:8px;line-height:1.8"><b>50+</b> <span style="font-size:5.5px">communities</span><br><b>12K+</b> <span style="font-size:5.5px">members</span><br><b>18</b> <span style="font-size:5.5px">states</span></div>
    <div class="a mono" style="left:10px;top:80px;font-size:7px;line-height:1.3">Growing<br>every week.</div>
    <div class="photo" role="img" aria-label="Map of member locations marked in red" style="left:96px;top:14px;width:130px;height:80px;background:radial-gradient(ellipse,#b9b5ab,#e4e1d8 75%)"></div>
  </div>
  <div class="card" style="left:255px;top:222px;width:257px;height:106px;background:#0f0f0f">
    <div class="photo" role="img" aria-label="Intense close portrait of a man in shadow" style="left:130px;top:0;width:127px;height:106px;background:linear-gradient(90deg,#0f0f0f,#4a4640 60%,#1a1917)"></div>
    <div class="a display" style="left:12px;top:12px;font-size:22px;line-height:.95">This isn't<br>therapy.<br><span style="color:var(--red)">It's<br>training.</span></div>
    <div class="a" style="right:10px;bottom:10px;width:8px;height:8px;background:var(--orange)"></div>
  </div>
</section>

<!-- 07 WHITE PAPER -->
<section class="panel" style="left:10px;top:776px;width:505px;height:212px">
  <h2 class="p-title">07. White Paper / Editorial Style</h2>
  <p class="p-sub">Premium. Tactical. Underground publication.<br>Not a typical report.</p>
  <div class="card" style="left:20px;top:50px;width:118px;height:150px;background:#1a1a1a;border:1px solid #333">
    <div class="a mono" style="left:8px;top:8px;font-size:6.5px;line-height:1.3;color:#ccc">Brash Ward<br>White paper</div>
    <div class="a display" style="left:8px;top:36px;font-size:16px;line-height:.94">The<br>physical<br>solution<br>to a mental<br>health crisis</div>
    <div class="a" style="left:8px;bottom:10px;width:7px;height:7px;background:#ddd"></div>
    <div class="a mono" style="right:8px;bottom:8px;font-size:6px;color:#aaa">2024</div>
  </div>
  <div class="card" style="left:147px;top:46px;width:176px;height:154px;background:#2a2a2a">
    <div class="photo" role="img" aria-label="Man working through a hard training set" style="left:70px;top:0;width:106px;height:154px;background:linear-gradient(90deg,#2a2a2a,#6b6863 50%,#3a3835)"></div>
    <div class="a display" style="left:8px;top:10px;font-size:40px">01</div>
    <div class="a display" style="left:8px;top:56px;font-size:15px">The problem</div>
    <div class="a mono" style="left:8px;top:80px;font-size:5px;line-height:1.5;color:#bbb;width:70px">Men are told to sit still and talk it out. Most never show up. The gap is action.</div>
  </div>
  <div class="card" style="left:327px;top:46px;width:168px;height:154px;background:var(--bone);color:#111">
    <div class="a display" style="left:8px;top:8px;font-size:14px">The statistics</div>
    <div class="a display" style="left:8px;top:30px;font-size:36px">70%</div>
    <div class="a mono" style="left:8px;top:66px;font-size:5.5px">Of men suffer in silence.</div>
    <div class="a mono" style="left:92px;top:30px;width:70px;font-size:4.5px;line-height:1.5;color:#444">Isolation grows fast. Movement and crew break the cycle early.</div>
    <div class="a" style="left:8px;top:86px;width:74px;height:58px;background:#111;color:var(--bone)"><div class="a display" style="left:6px;top:6px;font-size:18px">3X</div><div class="a mono" style="left:6px;top:32px;font-size:4.5px;width:60px">more likely to stay</div></div>
    <div class="a" style="left:86px;top:86px;width:74px;height:58px;background:#111;color:var(--bone)"><div class="a display" style="left:6px;top:6px;font-size:18px">2.5X</div><div class="a mono" style="left:6px;top:32px;font-size:4.5px;width:60px">stronger support</div></div>
  </div>
</section>

<!-- EDITORIAL ELEMENTS -->
<section class="panel" style="left:524px;top:776px;width:476px;height:212px">
  <h2 class="p-title" style="font-size:13px">Editorial Elements</h2>
  <p class="p-sub" style="top:21px">Designed to make content<br>easy to scan and impactful.</p>
  <div class="card" style="left:10px;top:46px;width:146px;height:110px;background:var(--bone);color:#111">
    <div class="a display" style="left:8px;top:8px;font-size:25px;line-height:.94;letter-spacing:-.8px">“Comfort<br>is the enemy<br>of growth.”</div>
    <div class="a mono" style="left:8px;top:96px;font-size:5px">Field notes, vol. 1</div>
  </div>
  <div class="card" style="left:10px;top:160px;width:146px;height:46px;background:var(--bone)">
    <div class="a mono" style="left:8px;top:4px;font-size:6.5px;color:#111">Margin notes</div>
    <div class="a" style="left:22px;top:14px;font:600 14px/1 'Caveat',cursive;color:var(--orange);transform:rotate(-4deg)">This is where<br>change begins.</div>
  </div>
  <div class="box" style="left:164px;top:6px;width:130px;height:106px;background:#ece9e0">
    <div class="box-label" style="color:#111;font-size:7px">Callout box</div>
    <div class="a" style="left:10px;top:20px;width:108px;height:78px;background:var(--acid);color:#111;padding:6px">
      <div class="cond" style="font-size:10px;font-weight:700">Key takeaway</div>
      <div class="mono" style="font-size:7px;line-height:1.35;text-transform:none;letter-spacing:0">Movement creates chemical change. Chemical change creates mental change.</div>
    </div>
  </div>
  <div class="box" style="left:164px;top:122px;width:130px;height:82px;background:#ece9e0">
    <div class="box-label" style="color:#111;font-size:7px">Stamp / label</div>
    <div class="a" style="left:16px;top:18px;width:74px;height:54px;border:2px solid #222;border-radius:4px;transform:rotate(-5deg);font:400 14px/1.05 'Special Elite',monospace;color:#222;padding:4px 6px;text-transform:uppercase">Field<br>report<br>#02</div>
  </div>
  <div class="box" style="left:302px;top:6px;width:164px;height:113px;background:#ece9e0">
    <div class="box-label" style="color:#111;font-size:7px">Chapter divider</div>
    <div class="photo" role="img" aria-label="Lone figure standing on a rocky ridge" style="left:80px;top:16px;width:84px;height:97px;background:linear-gradient(180deg,#d3d0c8,#3a3a3a)"></div>
    <div class="a display" style="left:10px;top:16px;font-size:50px;color:#111">02</div>
    <div class="a display" style="left:10px;top:72px;font-size:17px;color:#111">The<br>solution</div>
  </div>
  <div class="box" style="left:302px;top:124px;width:164px;height:80px;background:#ece9e0">
    <div class="box-label" style="color:#111;font-size:7px">Redactions</div>
    <div class="a" style="left:8px;top:18px;width:130px;height:8px;background:#111"></div>
    <div class="a" style="left:8px;top:31px;width:68px;height:8px;background:#111"></div>
    <div class="a mono" style="left:80px;top:30px;font-size:8px;color:#111;text-transform:none">The truth</div>
    <div class="a mono" style="left:8px;top:43px;font-size:8px;color:#111;text-transform:none">is uncomfortable.</div>
    <div class="a" style="left:8px;top:56px;width:140px;height:8px;background:#111"></div>
    <div class="a mono" style="left:8px;top:66px;font-size:8px;color:#111;text-transform:none">but necessary.</div>
    <div class="a" style="left:86px;top:68px;width:62px;height:8px;background:#111"></div>
  </div>
</section>

<!-- 08 STYLE REFERENCES -->
<section class="panel" style="left:1008px;top:776px;width:518px;height:212px">
  <h2 class="p-title">08. Style References</h2>
  <p class="p-sub">Cultural touchpoints that inspire the visual language.</p>
  <div class="a" style="left:6px;top:42px;width:111px;height:164px;background:#0e0e0e;border:1px solid #333">
    <div class="a mono" style="left:0;top:0;width:109px;height:16px;background:#d9d6cd;color:#111;font-size:6.5px;line-height:16px;text-align:center">Streetwear / culture</div>
    <div class="a mono" style="left:10px;top:32px;font-size:11px;font-weight:700">Ironclad Work</div>
    <div class="a mono" style="left:10px;top:66px;font-size:11px;font-weight:700">Hollow Yard</div>
    <div class="a mono" style="left:10px;top:100px;font-size:11px;font-weight:700">Lowline</div>
    <div class="a mono" style="left:10px;top:134px;font-size:11px;font-weight:700">Static Cell</div>
  </div>
  <div class="a" style="left:122px;top:42px;width:106px;height:164px;background:#0e0e0e;border:1px solid #333">
    <div class="a mono" style="left:0;top:0;width:104px;height:16px;background:#d9d6cd;color:#111;font-size:6px;line-height:16px;text-align:center">Editorial / typography</div>
    <div class="a mono" style="left:10px;top:32px;font-size:12px;font-weight:700">Issue 071</div>
    <div class="a mono" style="left:10px;top:70px;font-size:12px;font-weight:700">Fold Press</div>
    <div class="a mono" style="left:10px;top:110px;font-size:12px;font-weight:700">Front Page</div>
  </div>
  <div class="a" style="left:232px;top:42px;width:120px;height:164px;background:#0e0e0e;border:1px solid #333">
    <div class="a mono" style="left:0;top:0;width:118px;height:16px;background:#d9d6cd;color:#111;font-size:6.5px;line-height:16px;text-align:center">Posters / propaganda</div>
    <div class="card" style="left:4px;top:20px;width:54px;height:138px;background:var(--red)">
      <div class="a display" style="left:4px;top:6px;font-size:20px;color:#111">Resist</div>
      <div class="photo" role="img" aria-label="Raised fist poster artwork" style="left:6px;top:40px;width:42px;height:92px;background:linear-gradient(180deg,#8a0303,#2a0101)"></div>
    </div>
    <div class="card" style="left:62px;top:20px;width:54px;height:138px;background:#cfcabd">
      <div class="a display" style="left:4px;top:6px;font-size:15px;color:#111;line-height:.92">Power<br>to the<br>people</div>
      <div class="photo" role="img" aria-label="Crowd march poster artwork" style="left:4px;top:60px;width:46px;height:72px;background:linear-gradient(180deg,#8f8a7e,#2b2925)"></div>
    </div>
  </div>
  <div class="a" style="left:357px;top:42px;width:155px;height:164px;background:#0e0e0e;border:1px solid #333">
    <div class="a mono" style="left:0;top:0;width:153px;height:16px;background:#d9d6cd;color:#111;font-size:6.5px;line-height:16px;text-align:center">Documentary / manuals</div>
    <div class="a" style="left:4px;top:20px;width:70px;height:138px;background:#3b3a32">
      <div class="a mono" style="left:6px;top:18px;font-size:7px;line-height:1.3;color:#d6d2c4">Field<br>manual<br>FM 09-12</div>
      <div class="a" style="left:22px;top:96px;width:26px;height:26px;border-radius:50%;background:#23221d"></div>
    </div>
    <div class="a" style="left:78px;top:20px;width:72px;height:138px;background:#9a7b52">
      <div class="a cond" style="left:6px;top:36px;font-size:10px;font-weight:700;line-height:1.15;color:#1a140c">Recon<br>unit<br>handbook</div>
      <div class="a" style="left:24px;top:100px;width:22px;height:22px;border-radius:50%;background:#6e5638"></div>
    </div>
  </div>
</section>

<footer class="footer">
  <div class="a brandname" style="left:36px;top:10px;font-size:12px;color:#ddd"><i style="background:var(--orange);width:10px;height:10px"></i>Brash Ward</div>
  <div class="a cond" style="left:498px;top:6px;font-size:15px;font-weight:500;letter-spacing:1.2px;color:var(--orange)">Movement. Discipline. Community. Purpose.</div>
  <div class="a mono" style="right:134px;top:8px;font-size:12px;font-style:italic;color:#ddd">Real men. Real struggles. Real strength.</div>
</footer>

</div>
</body>
</html>
```